I need to redesign this website. Modern Fun Professional Redesign For www.JollyPerkHub.com = New Name www.ClaimVouchly.com

Use existing content as it is on website exactly and we will revise after initial mock ups.

The new name will be ClaimVouchly.com please make a quick logo for this site too while redesigning.

Make it look like an official website....

Target Market(s)

Consumers that are redeeming certificates that businesses gave to them as a gift for customer loyalty,e tc.

Industry/Entity Type

It Professional

Logo Text

www.ClaimVouchly.com

Number of Pages Required

4 page

Colors

Designer to choose colors to be used in the design.

Requirements
Must have
• Must look professional, build trust and credibility.
Nice to have
• open
Should not have
• open

```html
<!DOCTYPE html>
<html lang="en">
<head>
<meta charset="utf-8">
<title>ClaimVouchly.com – The Redemption Source</title>
<link href="https://fonts.googleapis.com/css2?family=Raleway:wght@400;500;600;700&display=swap" rel="stylesheet">
<style>
:root{
  --navy:#2e4169;
  --navy-line:#40537c;
  --orange:#f26322;
  --hero-a:#f0a57c;
  --hero-b:#d9875c;
  --text:#2e3a5c;
  --white:#ffffff;
  --rule:#b8c6da;
}
*{margin:0;padding:0;box-sizing:border-box}
html,body{width:1200px;height:2179px;overflow:hidden;background:var(--white)}
body{font-family:'Raleway',sans-serif;color:var(--text);position:relative}
.abs{position:absolute}

/* header */
.site-header{position:absolute;left:0;top:0;width:1200px;height:84px;background:var(--navy)}
.brand{position:absolute;left:140px;top:24px;display:flex;align-items:center;gap:10px;color:var(--orange);font-weight:700;font-size:32px}
.brand-dot{width:30px;height:30px;border-radius:50%;background:var(--orange)}
.main-nav{position:absolute;left:628px;top:0;display:flex;height:84px}
.main-nav a{display:flex;align-items:center;justify-content:center;color:var(--white);text-decoration:none;font-size:15px;font-weight:600;border-left:1px solid var(--navy-line);height:84px}
.main-nav a.active{background:var(--orange);border-left:none}

/* hero */
.hero{position:absolute;left:0;top:84px;width:1200px;height:585px;background:linear-gradient(180deg,var(--hero-a),var(--hero-b));color:var(--white);text-align:center}
.hero-title{position:absolute;left:0;width:1200px;top:72px;font-size:41px;font-weight:700;letter-spacing:.5px}
.hero-prompt{position:absolute;left:0;width:1200px;top:188px;font-size:14px;font-weight:600;line-height:19px;text-transform:uppercase}
.cert-form{position:absolute;left:305px;top:233px;display:flex}
.cert-input{width:527px;height:47px;border:none;background:var(--white)}
.cert-go{width:61px;height:47px;border:none;background:var(--navy);color:var(--white);font-family:inherit;font-weight:700;font-size:15px}
.hero-copy{position:absolute;left:230px;width:740px;top:304px;font-size:21px;font-weight:500;line-height:26px}
.hero-copy p{margin-bottom:25px}

/* sections */
.section-title{position:absolute;left:36px;color:var(--orange);font-weight:700;font-size:20px}
.testimonial{position:absolute;top:746px;width:275px;font-size:14px;line-height:17px}
.testimonial .who{margin-top:16px}
.testimonial .where{margin-top:16px}
.btn-outline{position:absolute;border:2px solid var(--orange);color:var(--orange);background:var(--white);font-family:inherit;font-weight:700;display:flex;align-items:center;justify-content:center;letter-spacing:2px}

.label-orange{position:absolute;left:36px;color:var(--orange);font-weight:700}
.mail-addr{position:absolute;left:37px;top:1092px;font-size:18px;line-height:21px}
.form-note{position:absolute;left:36px;top:1221px;font-size:12px;line-height:15px;width:450px}
.field{position:absolute;left:36px;width:575px;border-bottom:1.5px solid var(--rule);color:var(--orange);font-weight:700;font-size:17px;padding-bottom:8px}

.help-panel{position:absolute;left:681px;top:1299px;width:519px;height:356px;background:linear-gradient(135deg,#e29a72,#d47f55)}
.help-tag{position:absolute;left:982px;top:1299px;width:218px;height:46px;background:var(--navy);color:var(--white);font-weight:600;font-size:18px;display:flex;align-items:center;justify-content:center}
.help-copy{position:absolute;left:1008px;top:1380px;width:190px;color:var(--white);font-size:17px;line-height:21px}

.footnote{position:absolute;left:36px;top:2064px;width:350px;font-size:11px;line-height:13px}
.footnote u{text-decoration:underline}
</style>
</head>
<body>

<header class="site-header">
  <div class="brand"><span class="brand-dot"></span>ClaimVouchly.com</div>
  <nav class="main-nav">
    <a class="active" style="width:84px">HOME</a>
    <a style="width:131px">CONTACT US</a>
    <a style="width:132px">TESTIMONIALS</a>
    <a style="width:79px">TERMS</a>
  </nav>
</header>

<section class="hero">
  <div role="img" aria-label="Hand reaching up against a sunlit city skyline, orange toned" style="position:absolute;inset:0"></div>
  <h1 class="hero-title">WELCOME TO THE REDEMPTION SOURCE</h1>
  <p class="hero-prompt">Please enter a valid certificate ID in the form below<br>to redeem your certificate and to view FAQ's, terms and locations.</p>
  <form class="cert-form"><input class="cert-input" type="text" aria-label="Certificate ID"><button class="cert-go" type="button">GO</button></form>
  <div class="hero-copy">
    <p>ClaimVouchly.com is a leading company in travel certificate fulfillment.</p>
    <p>Our goal is to make it easy for you to redeem your certificate and our philosophy is this: <b>"What good is it to receive a gift certificate if you can't use it?".</b></p>
    <p>If you have any questions about how to redeem a certain certificate, please contact us. We are here to help.</p>
  </div>
</section>

<h2 class="section-title" style="top:702px">TESTIMONIALS</h2>
<div class="testimonial" style="left:36px">
  <p>"Nora was a 'saving grace.' She followed up and helped me book the vacation and air fare. Nora was positive and did everything she promised to do."</p>
  <p class="who">Helen T.</p><p class="where">Athens, GA</p>
</div>
<div class="testimonial" style="left:368px">
  <p>"Daniel was able to put together our flight schedule. He was very patient with us and diligent in working out all the changes I was requesting. Thank you, Dan."</p>
  <p class="who">Mary Beth K.</p><p class="where">Mesa, AZ</p>
</div>
<div class="testimonial" style="left:700px">
  <p>"Our vacation was great!!!! We stayed at the Silverpalm. And we had a lot of fun. We do not have any pictures as everyone else took them. We celebrated our grandson's 21st birthday."</p>
  <p class="who">Ruth P.</p><p class="where">West Fargo, ND</p>
</div>
<div class="btn-outline" style="left:1011px;top:852px;width:138px;height:46px;font-size:15px">VIEW MORE</div>

<h2 class="section-title" style="top:970px">CONTACT US</h2>
<div class="label-orange" style="top:1055px;font-size:18px">MAILING ADDRESS:</div>
<address class="mail-addr" style="font-style:normal">The Redemption Center<br>2250 Harbor Crest Rd Ste 4 #118<br>Linden Vale, Ca 90000</address>
<div class="label-orange" style="top:1177px;font-size:18px">SUBMIT YOUR INFORMATION BELOW AND YOU WILL BE CONTACTED WITHIN 1 BUSINESS DAY.</div>
<p class="form-note">You Must Fill In All Fields Below In Order For Us To Assist You. Incomplete information could result in no contact at all.</p>

<div class="field" style="top:1295px">NAME</div>
<div class="field" style="top:1350px">CERTIFICATE ID #:</div>
<div class="field" style="top:1406px">E-MAIL</div>
<div class="field" style="top:1461px">PHONE:</div>
<div class="field" style="top:1518px;height:214px">MESSAGE</div>

<div class="help-panel" role="img" aria-label="Smiling woman with glasses at a desk holding a mug, orange toned"></div>
<div class="help-tag">HAVE QUESTIONS?</div>
<p class="help-copy">We are here to help you redeem your certificates.<br>Feel free to contact us with any questions or suggestions on how e can do our job better.</p>

<div class="label-orange" style="top:1899px;font-size:17px">ENTER SECURITY CODE ABOVE:</div>
<div class="abs" style="left:36px;top:1974px;width:389px;border-bottom:1.5px solid var(--rule)"></div>
<div class="btn-outline" style="left:36px;top:2006px;width:141px;height:46px;font-size:14px;letter-spacing:1px">SUBMIT</div>
<p class="footnote">Please add <u>DoNotReply@JollyPerkHub.com</u> to your email safelist as this can help assure that you will receive our email response. Please note that that our emails could be sent to your junk or spam folders so please check there.</p>

</body>
</html>
```